Prominent Law Firm Needs a New Stationary Design

We need new stationary design to go with our new logo and rustic offices.
Things we need on the letterhead:
logo (see attached file), would also like the Multi-Million Dollar Logo (attached) somewhere on the stationary,
3182 North Pellam Street
Tulsa, Oklahoma 74105
(918) 555-0142 Tel ★ (918) 555-0187 Fax
www.TFWLAW.example

We also need the names of the 4 partners:
Dennis W. Hollister
Walter E. Hollister
Kevin M. Abernathy
Brian D. Whitcombe

And the other staff:
Janet K. Bowden
Tendai K. Chikwanda
Howard Pimsley

Lorraine F. Tuttle, RN

Of Counsel:
Prescott D. Hollister

```html
<!DOCTYPE html>
<html lang="en">
<head>
<meta charset="utf-8">
<title>Hollister Hollister Abernathy — Letterhead</title>
<link href="https://fonts.googleapis.com/css2?family=Open+Sans:wght@400;600;700&display=swap" rel="stylesheet">
<style>
  :root {
    --paper: #ffffff;
    --maroon: #771216;
    --ink: #2a2a2a;
    --sidebar-text: #f3e6e6;
    --sidebar-muted: #dcc4c4;
    --watermark: #ebebeb;
    --badge-ring: #d9b24a;
    --badge-core: #5a0d10;
  }
  * { margin: 0; padding: 0; box-sizing: border-box; }
  html, body {
    width: 1200px;
    height: 524px;
    overflow: hidden;
    background: var(--paper);
  }
  .letterhead {
    position: relative;
    width: 1200px;
    height: 524px;
    background: var(--paper);
    font-family: "Open Sans", Arial, sans-serif;
  }
  .sidebar {
    position: absolute;
    left: 39px;
    top: 0;
    width: 240px;
    height: 524px;
    background: var(--maroon);
    color: var(--sidebar-text);
    text-align: center;
  }
  .firm-mark {
    position: absolute;
    left: 45px;
    top: 14px;
    width: 150px;
    height: 150px;
    background: var(--paper);
    display: flex;
    flex-direction: column;
    align-items: center;
    justify-content: center;
    gap: 6px;
  }
  .firm-mark__initials {
    font-size: 40px;
    font-weight: 700;
    color: var(--ink);
    letter-spacing: 2px;
    line-height: 1;
  }
  .firm-mark__name {
    font-size: 9px;
    font-weight: 700;
    color: var(--ink);
    text-transform: uppercase;
    letter-spacing: 1px;
    line-height: 1.3;
    width: 120px;
  }
  .contact {
    position: absolute;
    left: 0;
    top: 176px;
    width: 240px;
    font-style: normal;
    font-size: 11.5px;
    line-height: 15px;
  }
  .contact__line--gap { margin-top: 4px; }
  .roster {
    position: absolute;
    left: 0;
    top: 254px;
    width: 240px;
    font-size: 10px;
    line-height: 13px;
    list-style: none;
  }
  .roster__group + .roster__group { margin-top: 6px; }
  .roster__label {
    font-weight: 600;
    color: var(--sidebar-muted);
    text-transform: uppercase;
    letter-spacing: 0.8px;
    font-size: 8.5px;
  }
  .badge {
    position: absolute;
    left: 85px;
    top: 416px;
    width: 70px;
    height: 70px;
  }
  .watermark {
    position: absolute;
    left: 500px;
    top: 262px;
    width: 440px;
    text-align: center;
    font-size: 140px;
    font-weight: 700;
    color: var(--watermark);
    letter-spacing: 4px;
    line-height: 1;
    user-select: none;
  }
</style>
</head>
<body>
  <main class="letterhead">
    <aside class="sidebar">
      <div class="firm-mark">
        <span class="firm-mark__initials">HHA</span>
        <span class="firm-mark__name">Hollister Hollister Abernathy</span>
      </div>
      <address class="contact">
        <div>North Pellam Street 3182</div>
        <div>Tulsa, Oklahoma 74105</div>
        <div class="contact__line--gap">(918) 555-0142 Tel ★ (918) 555-0187 Fax</div>
        <div>www.TFWLAW.example</div>
      </address>
      <ul class="roster">
        <li class="roster__group">
          <div>Dennis W. Hollister</div>
          <div>Walter E. Hollister</div>
          <div>Kevin M. Abernathy</div>
          <div>Brian D. Whitcombe</div>
        </li>
        <li class="roster__group">
          <div>Janet K. Bowden</div>
          <div>Tendai K. Chikwanda</div>
          <div>Howard Pimsley</div>
          <div>Lorraine F. Tuttle, RN</div>
        </li>
        <li class="roster__group">
          <div class="roster__label">Of Counsel</div>
          <div>Prescott D. Hollister</div>
        </li>
      </ul>
      <svg class="badge" viewBox="0 0 70 70" role="img" aria-label="Award badge">
        <circle cx="35" cy="35" r="34" fill="var(--paper)"/>
        <circle cx="35" cy="35" r="29" fill="var(--badge-ring)"/>
        <circle cx="35" cy="35" r="20" fill="var(--badge-core)"/>
      </svg>
    </aside>
    <div class="watermark" aria-hidden="true">HHA</div>
  </main>
</body>
</html>
```